Business card design for Velvet Harbor

We need business cards designed for our new marketing consulting company, Velvet Harbor. Our services include marketing strategy, go-to-market and launch planning, growth strategy, and execution. We serve medical technology and health technology companies, from startups to well-established growth companies.

The business cards should feel professional, credible, reliable and trustworthy, and should instill confidence. Also bold, creative, and modern.

The design must use the Velvet Harbor logo.

The primary brand color is this orange: #FF5501
A secondary color that you can use is this gray: #282B2D
I would prefer only to use the orange and gray. But if you feel you really need an additional accent color (please use it very sparingly, as little as possible), you can use this blue for small accent purposes: #009FED

Attached are the logo files. The main logo is the one with a little bit of orange on the left and the rest is gray.

The business card should include the following:

Velvet Harbor logo
First name and last name
Title
Email address
Phone number and type (in whatever order looks best for the design
Website (the website does not need to be in the same block as the personal info)

For example:

Nessa Pryle
Founder & Principal
nessa@velvetharbor.com
+1.628.309.4156 mobile (can use "." or spaces in between blocks of numbers)
velvetharbor.com (somewhere on the card, it does not need to be with the personal info; and note that there is no "www." at the beginning)

Note that there will be no address listed on the business card.

Target Market(s)

Executives (CEO, head of marketing, head of sales) at medical technology and health technology companies, mostly in their 40s and older, well-educated, often with advanced degrees. They are strategic thinkers, responsible for budgets, and familiar with P&L. Their comfort with and trust in using outside consultants varies.

Industry/Entity Type

Medical technology and health technology companies.

Contact Information for Business Card

See project description

Font styles to use
Sans Serif

Requirements
Must have
• Logo and see Business card details section above.

```html
<!DOCTYPE html>
<html lang="en">
<head>
<meta charset="utf-8">
<title>Velvet Harbor — Business Card</title>
<link href="https://fonts.googleapis.com/css2?family=Montserrat:wght@400;500;600;700&display=swap" rel="stylesheet">
<style>
  :root {
    --orange: #FF5501;
    --gray: #282B2D;
    --ink-soft: #3a3d40;
    --card-dark: #1d1e1f;
    --card-light: #ffffff;
    --stage: #3b3c3d;
  }
  * { box-sizing: border-box; margin: 0; padding: 0; }
  html, body { width: 1200px; height: 689px; overflow: hidden; }
  body {
    background: var(--stage);
    font-family: "Montserrat", sans-serif;
    position: relative;
  }
  .card {
    position: absolute;
    top: 196px;
    width: 520px;
    height: 297px;
    border-radius: 18px;
    overflow: hidden;
  }
  .card--back { left: 50px; background: var(--card-dark); }
  .card--front { left: 630px; background: var(--card-light); }

  .back-texture {
    position: absolute; inset: 0;
    background: radial-gradient(circle at 50% 50%, #232425 0%, var(--card-dark) 70%);
  }
  .back-brand {
    position: absolute; left: 50%; top: 50%;
    transform: translate(-50%, -50%);
    display: flex; align-items: center; gap: 14px;
  }
  .brand-dot {
    width: 34px; height: 34px; border-radius: 50%;
    background: var(--orange);
    flex: none;
  }
  .brand-name {
    font-weight: 600;
    letter-spacing: 0.22em;
    text-transform: uppercase;
    line-height: 1.15;
  }
  .back-brand .brand-name { color: #ffffff; font-size: 21px; }

  .front-brand {
    position: absolute; left: 34px; top: 38px;
    display: flex; align-items: center; gap: 16px;
  }
  .front-brand .brand-dot { width: 46px; height: 46px; background: var(--gray); }
  .front-brand .brand-name { color: var(--gray); font-size: 25px; }

  .person { position: absolute; left: 34px; top: 140px; }
  .person-name {
    color: var(--orange); font-weight: 700; font-size: 24px; line-height: 1.1;
  }
  .person-title {
    color: var(--gray); font-weight: 500; font-size: 13px; margin-top: 5px;
  }
  .contacts { list-style: none; margin-top: 14px; }
  .contacts li {
    display: flex; align-items: center; gap: 9px;
    color: var(--ink-soft); font-size: 12px; line-height: 21px;
  }
  .contacts svg { width: 12px; height: 12px; flex: none; fill: var(--orange); }
  .contact-type { color: var(--orange); font-weight: 500; }
</style>
</head>
<body>

<section class="card card--back">
  <div class="back-texture" role="img" aria-label="Repeating pattern of raised ring marks in gloss black on matte black"></div>
  <div class="back-brand">
    <span class="brand-dot"></span>
    <span class="brand-name">Velvet<br>Harbor</span>
  </div>
</section>

<section class="card card--front">
  <div class="front-brand">
    <span class="brand-dot"></span>
    <span class="brand-name">Velvet<br>Harbor</span>
  </div>

  <div class="person">
    <h1 class="person-name">Nessa Pryle</h1>
    <p class="person-title">Founder &amp; Principal</p>
    <ul class="contacts">
      <li>
        <svg viewBox="0 0 24 24"><path d="M6.6 10.8a15 15 0 0 0 6.6 6.6l2.2-2.2c.3-.3.7-.4 1-.2 1.1.4 2.3.6 3.6.6.6 0 1 .4 1 1V20c0 .6-.4 1-1 1A17 17 0 0 1 3 4c0-.6.4-1 1-1h3.5c.6 0 1 .4 1 1 0 1.3.2 2.5.6 3.6.1.3 0 .7-.2 1z"/></svg>
        <span>+1.628.309.4156 <span class="contact-type">mobile</span></span>
      </li>
      <li>
        <svg viewBox="0 0 24 24"><path d="M2 5h20v14H2zM4 7v.5l8 5 8-5V7l-8 5z"/></svg>
        nessa@velvetharbor.com
      </li>
      <li>
        <svg viewBox="0 0 24 24"><path d="M12 2a10 10 0 1 0 0 20 10 10 0 0 0 0-20zm6.9 6h-3a15 15 0 0 0-1.3-3.9A8 8 0 0 1 18.9 8zM12 4c.8 1.2 1.5 2.5 1.9 4h-3.8c.4-1.5 1.1-2.8 1.9-4zM4.3 14a8 8 0 0 1 0-4h3.4a16 16 0 0 0 0 4zm.8 2h3a15 15 0 0 0 1.3 3.9A8 8 0 0 1 5.1 16zm3-8h-3a8 8 0 0 1 4.3-3.9C8.8 5.3 8.4 6.6 8.1 8zM12 20c-.8-1.2-1.5-2.5-1.9-4h3.8c-.4 1.5-1.1 2.8-1.9 4zm2.3-6H9.7a14 14 0 0 1 0-4h4.6a14 14 0 0 1 0 4zm.3 5.9c.6-1.2 1-2.5 1.3-3.9h3a8 8 0 0 1-4.3 3.9zm1.7-5.9a16 16 0 0 0 0-4h3.4a8 8 0 0 1 0 4z"/></svg>
        velvetharbor.com
      </li>
    </ul>
  </div>
</section>

</body>
</html>
```